Business Card Design Project

Brightwater Advisory is a newly created boutique consultancy focussing on delivering strategic consulting to medium and large businesses, with a focus on:
- Strategic planning and execution.
- Corporate function optimisation, especially in the areas of finance, commercial, and IT. This includes implementing the right functional design for the needs of the business, and ensuring the right skills.
- Performance management, in particular project governance and control, operational metrics and management reporting.
I have in mind a tag line for the business being:
"Helping business to discover sustainable value."
I am looking for a letterhead design which utilises my new logo on report templates (powerpoint and word), and letterhead.
Lexipoint defines a mother lode as follows:
"Mother lode is a principal vein or zone of veins of gold or silver ore. The term probably came from a literal translation of the Spanish veta madre, a term common in old Mexican mining. Veta madre, for instance, is the name given to an 11-kilometre-long (6.8 mi) silver vein discovered in 1548 in Guanajuato, New Spain (modern-day Mexico)."
My preference is for black and gold. Logo files are attached in .eps format. All fonts are outlined. The fonts that are used are "Crimson Text" and "Josefin Sans". They are free open source fonts and they are available here: http://www.typevault-demo.net/fonts
Target Market(s)
Medium to large corporates.
Industry/Entity Type
Boutique
Other font styles liked:
- All Fonts Are Outlined. The Fonts That Are Used Are "Crimson Text" And "Josefin Sans". They Are Free Open Source Fonts And They Are Available Here: Http://www.typevault-demo.net/fonts

```html
<!DOCTYPE html>
<html lang="en">
<head>
<meta charset="utf-8">
<title>Brightwater Advisory – Business Card</title>
<link rel="stylesheet" href="https://fonts.googleapis.com/css2?family=Crimson+Text:wght@400;600&family=Questrial&display=swap">
<style>
  :root {
    --gold: #e0a431;
    --ink: #111111;
    --ink-soft: #222222;
    --paper: #ffffff;
    --stage: #e7e5e1;
    --grey-text: #cfcfcf;
  }
  * { margin: 0; padding: 0; box-sizing: border-box; }
  html, body { width: 1200px; height: 784px; overflow: hidden; }
  body { background: var(--stage); position: relative; font-family: "Questrial", sans-serif; }

  .card {
    position: absolute;
    top: 238px;
    width: 540px;
    height: 309px;
    overflow: hidden;
    box-shadow: 0 6px 18px rgba(0,0,0,0.18);
  }
  .card--front { left: 40px; background: radial-gradient(ellipse at 50% 40%, #262626 0%, var(--ink) 75%); }
  .card--back { left: 620px; background: var(--paper); }

  /* front */
  .front-mark {
    position: absolute; left: 236px; top: 42px;
    width: 68px; height: 68px;
    border: 7px solid var(--paper);
  }
  .front-name {
    position: absolute; left: 0; right: 0; top: 126px;
    text-align: center;
    font-family: "Crimson Text", serif; font-weight: 400;
    font-size: 38px; letter-spacing: 2px; color: var(--paper);
    text-transform: uppercase;
  }
  .front-tagline {
    position: absolute; left: 0; right: 0; top: 186px;
    text-align: center;
    font-family: "Crimson Text", serif; font-size: 10px;
    letter-spacing: 2px; color: var(--grey-text); text-transform: uppercase;
  }

  /* back */
  .holder { position: absolute; right: 22px; top: 20px; text-align: right; line-height: 1.15; }
  .holder__name { color: var(--gold); font-size: 15px; }
  .holder__role { color: var(--ink); font-size: 12px; }

  .back-mark {
    position: absolute; left: 52px; top: 72px;
    width: 62px; height: 62px;
    border: 6px solid var(--ink);
  }
  .back-name {
    position: absolute; left: 128px; top: 84px;
    font-family: "Crimson Text", serif; font-weight: 400;
    font-size: 31px; letter-spacing: 1px; color: var(--ink);
    text-transform: uppercase;
  }

  .tag-band {
    position: absolute; left: 0; right: 0; top: 148px; height: 24px;
    background: var(--gold);
    padding-left: 52px;
    font-size: 15px; line-height: 24px; letter-spacing: 1px; color: var(--ink);
  }
  .contact-panel {
    position: absolute; left: 0; right: 0; top: 172px; bottom: 0;
    background: linear-gradient(180deg, var(--ink-soft), var(--ink));
  }
  .contact-list { list-style: none; position: absolute; left: 40px; top: 12px; }
  .contact-list li {
    display: flex; align-items: center; gap: 6px;
    height: 23px; font-size: 16px; color: var(--paper);
  }
  .contact-list svg { width: 17px; height: 17px; flex: none; }
  .contact-list .indent { padding-left: 23px; }
</style>
</head>
<body>

<section class="card card--front" aria-label="Card front">
  <div class="front-mark"></div>
  <h1 class="front-name">Brightwater Advisory</h1>
  <p class="front-tagline">Helping business discover sustainable value</p>
</section>

<section class="card card--back" aria-label="Card back">
  <div class="holder">
    <p class="holder__name">Dana Whitfield</p>
    <p class="holder__role">Manager</p>
  </div>
  <div class="back-mark"></div>
  <h2 class="back-name">Brightwater Advisory</h2>
  <div class="tag-band">Helping business to discover sustainable value</div>
  <div class="contact-panel">
    <ul class="contact-list">
      <li>
        <svg viewBox="0 0 20 20" aria-hidden="true"><path fill="#e0a431" d="M5 2l3 4-2 2c1 2.5 3 4.5 5.5 5.5l2-2 4 3-1.5 3C9 17 3 11 2 4z"/></svg>
        (08) 5550 0142
      </li>
      <li>
        <svg viewBox="0 0 20 20" aria-hidden="true"><g fill="none" stroke="#e0a431" stroke-width="1.6"><circle cx="10" cy="10" r="8"/><ellipse cx="10" cy="10" rx="3.5" ry="8"/><path d="M2 10h16M3.5 6h13M3.5 14h13"/></g></svg>
        www.brightwater-demo.com
      </li>
      <li>
        <svg viewBox="0 0 20 20" aria-hidden="true"><rect x="2" y="4" width="16" height="12" fill="#e0a431"/><path d="M2 4l8 7 8-7" fill="none" stroke="#111" stroke-width="1.4"/></svg>
        hello@brightwater-demo.com
      </li>
      <li>
        <svg viewBox="0 0 20 20" aria-hidden="true"><path fill="#e0a431" d="M10 2l8 7h-2.5v9h-4v-5h-3v5h-4V9H2z"/></svg>
        PO Box 418 harbour street
      </li>
      <li class="indent">Clearwell, Western Australia, 6999</li>
    </ul>
  </div>
</section>

</body>
</html>
```